LinkedIn Engagement Posts for Bookkeeping Company

The task is to complete 20 engaging posts for our LinkedIn page. These posts should ask a question, take a poll, provide useful information or interesting articles. These should NOT be advertisements for our services. Our target audience is business owners (small and mid-size businesses). The content should be relevant to business owners/entrepreneurs. Topics should include content about making money, accounting/bookkeeping info, operating a business, cashflow, etc.

We use QuickBooks Online for our services, so do not refer to any other accounting software (unless it is a comparison showing advantages of QBO).

Our website:
https://www.fernhollowaccounting.com/

Target Market(s)

Business owners/entrepreneurs (Small & Mid-Sized Businesses)

Industry/Entity Type

Accounting company that provides bookkeeping services, financial reporting and payroll processing (does not provide tax services!)

Font styles to use
Serif
Sans Serif

Colors
0054AA
0677BA
7BADD7
CADEEF
E8F1F8

Requirements
Must have
• 20 Engaging posts for LinkedIn, including hashtags
Nice to have
• Stay with current branding for overall design graphics (see website and social media accounts)
Should not have
• We do not provide tax or audit services, so please do not include these topics other that to say you must have accurate and updated bookkeeping in order to complete taxes and/or in the event of an audit.

```html
<!DOCTYPE html>
<html lang="en">
<head>
<meta charset="utf-8">
<title>Fern Hollow Accounting – Bookkeeping Quote</title>
<link rel="stylesheet" href="https://fonts.googleapis.com/css2?family=Archivo:ital,wght@0,700;1,400;1,700&display=swap">
<style>
  :root {
    --brand-navy: #0a4a8c;
    --quote-teal: #3ab3cf;
    --mark-teal: #a8d5df;
    --card-tint: #d8eef3;
    --floor-tint: #e9f2f5;
    --paper: #ffffff;
  }
  * { margin: 0; padding: 0; box-sizing: border-box; }
  html, body { width: 1200px; height: 1200px; overflow: hidden; background: var(--paper); }
  .post {
    position: relative;
    width: 1200px;
    height: 1200px;
    overflow: hidden;
    background: var(--paper);
    font-family: "Archivo", "Helvetica Neue", Arial, sans-serif;
  }
  .backdrop { position: absolute; inset: 0; }
  .brand {
    position: absolute;
    top: 150px;
    left: 0;
    width: 1200px;
    display: flex;
    justify-content: center;
    align-items: center;
    gap: 14px;
  }
  .brand-dot {
    width: 22px;
    height: 22px;
    border-radius: 50%;
    background: var(--brand-navy);
  }
  .brand-name {
    font-weight: 700;
    font-size: 34px;
    color: var(--brand-navy);
    letter-spacing: 0.5px;
  }
  .quote-card {
    position: absolute;
    left: 207px;
    top: 352px;
    width: 791px;
    height: 628px;
    background: var(--paper);
    border-radius: 8px;
    box-shadow: 0 18px 40px rgba(60, 110, 130, 0.16);
  }
  .quote-text {
    position: absolute;
    left: 292px;
    top: 514px;
    font-style: italic;
    font-weight: 400;
    font-size: 36px;
    line-height: 55px;
    color: var(--quote-teal);
  }
  .quote-text strong {
    font-weight: 700;
    font-size: 38px;
    letter-spacing: 0.3px;
  }
  .quote-author {
    position: absolute;
    right: 314px;
    top: 798px;
    font-weight: 700;
    font-size: 22px;
    color: var(--quote-teal);
  }
  .quote-marks { position: absolute; inset: 0; pointer-events: none; }
</style>
</head>
<body>
<main class="post">
  <svg class="backdrop" width="1200" height="1200" viewBox="0 0 1200 1200" aria-hidden="true">
    <polygon points="0,822 1200,530 1200,1200 0,1200" fill="var(--floor-tint)"/>
    <rect x="282" y="287" width="628" height="786" rx="40" fill="var(--card-tint)" transform="rotate(-3.4 596 680)"/>
    <g stroke="var(--quote-teal)" stroke-width="4" fill="none">
      <line x1="906" y1="248" x2="948" y2="248"/>
      <line x1="927" y1="227" x2="927" y2="269"/>
      <line x1="102" y1="897" x2="144" y2="897"/>
      <line x1="123" y1="876" x2="123" y2="918"/>
      <circle cx="1006" cy="487" r="23"/>
      <circle cx="266" cy="1061" r="23"/>
    </g>
  </svg>

  <header class="brand">
    <span class="brand-dot"></span>
    <span class="brand-name">Fern Hollow Accounting</span>
  </header>

  <section class="quote-card"></section>

  <svg class="quote-marks" width="1200" height="1200" viewBox="0 0 1200 1200" aria-hidden="true">
    <g fill="var(--mark-teal)">
      <path d="M168,438 V385 Q168,350 222,345 V372 Q198,378 198,392 H222 V438 Z"/>
      <path d="M242,438 V385 Q242,350 296,345 V372 Q272,378 272,392 H296 V438 Z"/>
      <path d="M958,918 V971 Q958,1006 904,1011 V984 Q928,978 928,964 H904 V918 Z"/>
      <path d="M1032,918 V971 Q1032,1006 978,1011 V984 Q1002,978 1002,964 H978 V918 Z"/>
    </g>
  </svg>

  <p class="quote-text">
    It will be a<br>
    <strong>Book-keeping Nightmare</strong><br>
    to do this on paper and pencil<br>
    every month!
  </p>
  <p class="quote-author">~Daniel Marlowe</p>
</main>
</body>
</html>
```